Business Card Design for Oncology Consulting Company

We need a business card design using a logo that has already been created.

Company name is: ORBVA - Guild for Lumora Mapping, Welfare and Outreach

We would also like to include the following pieces of information on the business card:
Name
Title
US Address (street, city, state, zip, country)
Email address
Website address

Target Market(s)

The target customers are physicians (oncologists, pathologists) in Greece, Iran, US, etc who would refer patients to our company for a second medical opinion/genetic counseling for cancer.

Industry/Entity Type

Business

Colors

Designer to choose colors to be used in the design.

Requirements
Must have
• Must contain logo in attached file and elements described above.

```html
<!DOCTYPE html>
<html lang="en">
<head>
<meta charset="utf-8">
<title>ORBVA Business Card</title>
<link href="https://fonts.googleapis.com/css2?family=Ubuntu:wght@400;500;700&display=swap" rel="stylesheet">
<style>
  :root {
    --brand-blue: #0f5d9c;
    --card-blue: #1170b5;
    --ink-grey: #8f9398;
    --line-grey: #b9bcc0;
    --paper: #ffffff;
    --backdrop: #e6e7e9;
    --tag-light: #cfe2f2;
  }
  * { margin: 0; padding: 0; box-sizing: border-box; }
  html, body {
    width: 1200px; height: 900px; overflow: hidden;
    background: var(--backdrop);
    font-family: "Ubuntu", Arial, sans-serif;
  }
  .canvas {
    width: 1200px; height: 900px;
    display: flex; flex-direction: column;
    align-items: center; justify-content: center; gap: 56px;
  }
  .card {
    position: relative;
    width: 630px; height: 360px;
    box-shadow: 0 6px 18px rgba(0,0,0,0.18);
  }
  /* Front */
  .card-front { background: var(--paper); }
  .brand {
    position: absolute; left: 40px; top: 40px;
    display: flex; flex-direction: column; gap: 8px;
  }
  .brand-row { display: flex; align-items: center; gap: 14px; }
  .brand-name {
    font-weight: 700; font-size: 68px; line-height: 1;
    color: var(--brand-blue); letter-spacing: 1px;
  }
  .brand-dot {
    width: 16px; height: 16px; border-radius: 50%;
    background: var(--brand-blue);
  }
  .brand-tagline {
    font-size: 9px; font-weight: 500; text-transform: uppercase;
    letter-spacing: 0.6px; color: var(--ink-grey);
    border-top: 1.5px solid var(--line-grey); padding-top: 4px;
  }
  .contact {
    position: absolute; right: 40px; top: 150px;
    text-align: right;
  }
  .person-name {
    font-size: 15px; font-weight: 500; color: var(--brand-blue);
    text-transform: uppercase; letter-spacing: 0.3px;
  }
  .person-title {
    font-size: 15px; font-weight: 500; color: var(--brand-blue);
    margin-bottom: 14px;
  }
  .contact-lines {
    font-size: 15px; color: var(--ink-grey); line-height: 1.35;
    margin-bottom: 12px;
  }
  .address { font-size: 15px; color: var(--ink-grey); line-height: 1.35; }
  /* Back */
  .card-back { background: var(--card-blue); }
  .back-rule {
    position: absolute; left: 150px; right: 0; top: 196px;
    height: 2px; background: var(--line-grey);
  }
  .back-tagline {
    position: absolute; right: 30px; top: 206px;
    font-size: 10px; font-weight: 500; text-transform: uppercase;
    letter-spacing: 0.7px; color: var(--tag-light);
  }
</style>
</head>
<body>
<main class="canvas">
  <section class="card card-back" aria-label="Card back">
    <div class="back-rule"></div>
    <p class="back-tagline">Guild for Lumora Mapping, Welfare and Outreach</p>
  </section>

  <section class="card card-front" aria-label="Card front">
    <div class="brand">
      <div class="brand-row">
        <span class="brand-name">ORBVA</span>
        <span class="brand-dot"></span>
      </div>
      <p class="brand-tagline">Guild for Lumora Mapping, Welfare and Outreach</p>
    </div>
    <div class="contact">
      <p class="person-name">Darren Holloway</p>
      <p class="person-title">managing director</p>
      <div class="contact-lines">
        <p>555 010 24 68</p>
        <p>dholloway@orbva.com</p>
        <p>www.orbva.com</p>
      </div>
      <div class="address">
        <p>48 Linden Row</p>
        <p>Maple Falls, New York 12045</p>
      </div>
    </div>
  </section>
</main>
</body>
</html>
```